Tradie Thursday - A5 double sided pamphlet/brochure

We need a 1 page, double sided brochure made for a new themed night at our club…Tradie Thursday.

Our club is Velvetlane Lounge 47. However, this brochure is to have nothing sexual about it.

The theme is to be "Tradies"... Tradesman - painters, builders etc

We want it to be fairly simple. Very easy to read and to the point.

I have attached our logo - MUST BE ON THE BROCHURE

I have also attached a rough draft of the look. But it is very basic. We want something that looks much better than this! You DO NOT need to follow this layout.

This is to be a 1 Page, double sided, size: A5

It is to have the following information:

Title: Tradie Thursday
Kicks off June 2nd
Bar snacks
Front door prices
Quarterdeck Bar access 3-9pm
Entry to main showroom after 9pm (dress code applies)

Lucky Draw every hour
Win: VIP Memberships, Entertainment vouchers and more!

Small text:
83 Wattle Rd, Melbourne
9351 7206
www.lounge47.com.au

Very small text:
Sexually explicit material may offend
18+ only

Target Market(s)

young men, in the tradesman field of work, men who drink/go out/hang with their mates.

Industry/Entity Type

Club

Requirements
Must have
• Must have our logo
Nice to have
• The tradesman theme means it is masculine and for workers.

So anything with hazzard tape, road signs, machinery etc (but still general enough for all fields of work)

We are a (strip) club. So something conservative but maybe beer, or a bit of a nightclub look to the front page will be fine.

The main thing is to keep it simple and easy to read.
Should not have
• Nothing sexual.

There are still some women in trade work, and we don't want to offend.

```html
<!DOCTYPE html>
<html lang="en">
<head>
<meta charset="utf-8">
<title>Tradie Thursday – Velvetlane Lounge 47</title>
<link rel="stylesheet" href="https://fonts.googleapis.com/css2?family=Archivo+Black&family=Roboto+Condensed:wght@400;700&display=swap">
<style>
  :root {
    --stage: #cfcac2;
    --ink-black: #0a0a0c;
    --navy-stone: #1f2236;
    --red: #e11b22;
    --steel: #9a9ca4;
    --hi-vis: #f4e12b;
    --white: #ffffff;
    --silver: #c9c9c9;
    --extrude: 1px 1px 0 #8d8d8d, 2px 2px 0 #7a7a7a, 3px 3px 0 #676767, 4px 4px 0 #555, 5px 5px 4px rgba(0,0,0,.6);
  }
  * { box-sizing: border-box; margin: 0; padding: 0; }
  html, body { width: 1200px; height: 824px; overflow: hidden; background: var(--stage); }
  .canvas { position: relative; width: 1200px; height: 824px; }

  .flyer { position: absolute; overflow: hidden; box-shadow: 0 6px 18px rgba(0,0,0,.35); }
  .flyer--back  { left: 49px;  top: 40px; width: 513px; height: 740px; background: var(--navy-stone); }
  .flyer--front { left: 611px; top: 28px; width: 568px; height: 760px; background: var(--ink-black); }
  .flyer__shapes { position: absolute; inset: 0; width: 100%; height: 100%; }

  .slant { position: absolute; transform: translate(-50%, -50%) rotate(-34deg); white-space: nowrap; text-align: center; }

  .brand { position: absolute; font-family: "Archivo Black", sans-serif; color: var(--white); line-height: 1.1; display: flex; align-items: center; gap: 8px; }
  .brand__dot { width: 10px; height: 10px; border-radius: 50%; background: var(--red); flex: none; }

  .title { font-family: "Archivo Black", sans-serif; color: var(--white); text-shadow: var(--extrude); }
  .kickoff { font-family: "Roboto Condensed", sans-serif; font-weight: 700; }

  /* details side */
  .flyer--back .brand { left: 58px; top: 60px; font-size: 17px; }
  .flyer--back .kickoff { left: 240px; top: 100px; font-size: 24px; color: var(--hi-vis); }
  .flyer--back .title { left: 213px; top: 197px; font-size: 37px; }
  .address { left: 322px; top: 226px; font-family: "Roboto Condensed", sans-serif; font-size: 13.5px; color: var(--white); }
  .perks { left: 318px; top: 370px; font-family: "Roboto Condensed", sans-serif; font-weight: 700; font-size: 24px; line-height: 1.15; color: var(--hi-vis); text-align: left; list-style: none; }
  .perks li::before { content: "• "; }
  .entry-note { left: 396px; top: 446px; font-family: "Roboto Condensed", sans-serif; font-weight: 700; font-size: 14px; line-height: 1.35; color: var(--white); }
  .beer { position: absolute; left: 14px; top: 500px; width: 80px; height: 86px; border-radius: 10px; background: linear-gradient(180deg, #f7f3e6 0%, #f7c64a 30%, #e59a17 75%, #b86f0c 100%); }
  .lucky { left: 140px; top: 494px; }
  .lucky__title { font-family: "Archivo Black", sans-serif; font-size: 32px; line-height: .95; color: var(--red); text-shadow: -1px -1px 0 var(--white), 1px -1px 0 var(--white), -1px 1px 0 var(--white), 1px 1px 0 var(--white), 3px 3px 4px rgba(0,0,0,.7); }
  .lucky__note { font-family: "Roboto Condensed", sans-serif; font-size: 11px; color: var(--white); margin-top: 3px; }
  .prizes { left: 282px; top: 578px; font-family: "Roboto Condensed", sans-serif; font-size: 18px; line-height: 1.1; color: var(--white); }
  .prizes__lead { font-size: 23px; display: block; margin-bottom: 3px; }

  /* cover side */
  .bottles { position: absolute; left: 0; top: 380px; width: 100%; height: 380px; background: linear-gradient(180deg, #0a0a0c 0%, #3c3c3e 22%, #9a9a9a 52%, #d8d8d8 74%, #6f6f70 100%); }
  .flyer--front .brand { left: 0; width: 100%; top: 122px; justify-content: center; font-size: 40px; text-align: center; }
  .flyer--front .slant { transform: translate(-50%, -50%) rotate(-37deg); }
  .flyer--front .kickoff { left: 333px; top: 383px; font-size: 25px; color: var(--silver); }
  .flyer--front .title { left: 288px; top: 486px; font-size: 46px; }
</style>
</head>
<body>
<main class="canvas">

  <section class="flyer flyer--back" aria-label="Tradie Thursday flyer, details side">
    <svg class="flyer__shapes" viewBox="0 0 513 740" preserveAspectRatio="none" aria-hidden="true">
      <polygon points="0,0 513,0 513,12 0,240" fill="var(--ink-black)"/>
      <polygon points="60,213 492,20 513,14 513,154 147,366" fill="var(--ink-black)"/>
      <line x1="0" y1="240" x2="495" y2="18" stroke="var(--red)" stroke-width="2.5"/>
      <line x1="147" y1="368" x2="513" y2="156" stroke="var(--steel)" stroke-width="3"/>
      <polygon points="0,484 150,372 470,740 0,740" fill="var(--ink-black)"/>
      <line x1="0" y1="484" x2="152" y2="372" stroke="var(--red)" stroke-width="2.5"/>
    </svg>

    <div class="brand"><span class="brand__dot"></span><span>Velvetlane<br>Lounge 47</span></div>
    <p class="slant kickoff">Kicks off June 2nd</p>
    <h1 class="slant title">TRADIE THURSDAY</h1>
    <p class="slant address">83 Wattle Rd, Melbourne | 9351 7206 | www.lounge47.com.au</p>
    <ul class="slant perks">
      <li>Bar snacks</li>
      <li>Front door prices</li>
      <li>Quarterdeck Bar</li>
      <li>Access 3-9pm</li>
    </ul>
    <p class="slant entry-note">Entry to main showroom after<br>9pm (dress code applies)</p>
    <div class="beer" role="img" aria-label="Illustration of a frothy mug of beer"></div>
    <div class="slant lucky">
      <p class="lucky__title">LUCKY<br>DRAW</p>
      <p class="lucky__note">*EVERY HOUR*</p>
    </div>
    <p class="slant prizes"><span class="prizes__lead">WIN...</span>VIP Memberships,<br>Entertainment<br>vouchers<br>and more!</p>
  </section>

  <section class="flyer flyer--front" aria-label="Tradie Thursday flyer, cover side">
    <div class="bottles" role="img" aria-label="Black and white photo of a back bar lined with spirit bottles"></div>
    <div class="brand"><span class="brand__dot"></span><span>Velvetlane<br>Lounge 47</span></div>
    <p class="slant kickoff">Kicks off June 2nd</p>
    <h2 class="slant title">TRADIE THURSDAY</h2>
  </section>

</main>
</body>
</html>
```